Harborline Motors LLC

Car Dealer Customer Service
Address: 2741 Linden Avenue, Shelbyville, TN 37162
web: www.harborlinemotorstn.net
email: harborlinemotorstn@mailbox-example.net
Phone: (931) 555-0148
Phone: (629) 555-0173

```html
<!DOCTYPE html>
<html lang="en">
<head>
<meta charset="utf-8">
<title>Harborline Motors — Business Card</title>
<link rel="stylesheet" href="https://fonts.googleapis.com/css2?family=Oswald:wght@600&family=Roboto:wght@400;700&display=swap">
<style>
  :root {
    --backdrop: #4f4f4f;
    --card-blue: #2282b6;
    --paper: #f3f4f6;
    --ink-white: #ffffff;
    --brand-blue: #1f6f9f;
  }
  * { box-sizing: border-box; margin: 0; padding: 0; }
  html, body { width: 1133px; height: 1200px; overflow: hidden; }
  body {
    background: var(--backdrop);
    position: relative;
    font-family: "Roboto", Arial, sans-serif;
  }
  .card {
    position: absolute;
    left: 204px;
    width: 724px;
    height: 412px;
    border-radius: 22px;
    background: var(--card-blue);
    overflow: hidden;
  }
  .card--front { top: 140px; }
  .card--back { top: 640px; }

  .front-panel {
    position: absolute;
    inset: 0;
    width: 100%;
    height: 100%;
  }
  .contact {
    position: absolute;
    left: 38px;
    top: 96px;
    color: var(--ink-white);
  }
  .contact__name {
    font-family: "Oswald", "Arial Narrow", sans-serif;
    font-weight: 600;
    font-size: 27px;
    letter-spacing: 0.2px;
    line-height: 1.2;
    text-transform: uppercase;
  }
  .contact__role {
    font-size: 16px;
    line-height: 1.3;
    margin-bottom: 18px;
  }
  .contact__address {
    font-size: 16px;
    line-height: 1.3;
    margin-bottom: 12px;
  }
  .contact__list { list-style: none; }
  .contact__item {
    display: flex;
    align-items: center;
    gap: 9px;
    font-size: 14px;
    line-height: 20px;
  }
  .contact__icon { width: 15px; height: 15px; flex: none; }

  .brand-name {
    position: absolute;
    left: 330px;
    right: 0;
    top: 200px;
    text-align: center;
    font-family: "Roboto", Arial, sans-serif;
    font-weight: 700;
    font-size: 23px;
    color: var(--brand-blue);
    letter-spacing: 0.5px;
  }

  .back-name {
    position: absolute;
    left: 0; right: 0;
    top: 165px;
    text-align: center;
    font-weight: 700;
    font-size: 40px;
    letter-spacing: 1px;
    color: var(--ink-white);
  }
  .back-web {
    position: absolute;
    left: 0; right: 0;
    top: 358px;
    text-align: center;
    font-size: 16px;
    letter-spacing: 2.6px;
    color: var(--ink-white);
  }
  .back-web strong { font-weight: 700; }
</style>
</head>
<body>

<section class="card card--front">
  <svg class="front-panel" viewBox="0 0 724 412" aria-hidden="true">
    <circle cx="570" cy="206" r="240" fill="var(--paper)"/>
  </svg>

  <div class="contact">
    <h1 class="contact__name">Daniel Whitmore</h1>
    <p class="contact__role">Founder &amp; CEO</p>
    <p class="contact__address">Car Dealer Customer Service<br>2741 Linden Avenue<br>Shelbyville, TN 37162</p>
    <ul class="contact__list">
      <li class="contact__item">
        <svg class="contact__icon" viewBox="0 0 24 24"><path fill="#fff" d="M6.6 10.8a15.1 15.1 0 0 0 6.6 6.6l2.2-2.2a1 1 0 0 1 1-.25 11.4 11.4 0 0 0 3.6.57 1 1 0 0 1 1 1V20a1 1 0 0 1-1 1A17 17 0 0 1 3 4a1 1 0 0 1 1-1h3.5a1 1 0 0 1 1 1c0 1.25.2 2.45.57 3.57a1 1 0 0 1-.25 1z"/></svg>
        (931) 555-0148
      </li>
      <li class="contact__item">
        <svg class="contact__icon" viewBox="0 0 24 24"><path fill="#fff" d="M6.6 10.8a15.1 15.1 0 0 0 6.6 6.6l2.2-2.2a1 1 0 0 1 1-.25 11.4 11.4 0 0 0 3.6.57 1 1 0 0 1 1 1V20a1 1 0 0 1-1 1A17 17 0 0 1 3 4a1 1 0 0 1 1-1h3.5a1 1 0 0 1 1 1c0 1.25.2 2.45.57 3.57a1 1 0 0 1-.25 1z"/></svg>
        (629) 555-0173
      </li>
      <li class="contact__item">
        <svg class="contact__icon" viewBox="0 0 24 24"><rect x="2" y="5" width="20" height="14" rx="1" fill="#fff"/><path d="M2.5 6l9.5 7 9.5-7" fill="none" stroke="var(--card-blue)" stroke-width="1.6"/></svg>
        harborlinemotorstn@mailbox-example.net
      </li>
      <li class="contact__item">
        <svg class="contact__icon" viewBox="0 0 24 24"><circle cx="12" cy="12" r="10" fill="#fff"/><path d="M6 8c2 0 3 1 3 3s2 2 2 4-1 3-1 4M15 5c-1 2 1 3 3 3s2 2 1 3" fill="none" stroke="var(--card-blue)" stroke-width="1.6"/></svg>
        www.harborlinemotorstn.net
      </li>
    </ul>
  </div>

  <p class="brand-name">HARBORLINE MOTORS</p>
</section>

<section class="card card--back">
  <p class="back-name">HARBORLINE MOTORS</p>
  <p class="back-web">www.<strong>harborlinemotorstn</strong>.net</p>
</section>

</body>
</html>
```